Smart, Classy, Conservative looking Legal Letterhead

I need a letterhead that when you look at it it "says to you " this is a well established law firm with very smart lawyers, which will one day be appearing before the Grand Bench of the USA. All information about the Law firm should appear at the top of the page. please no information in the footer.

Legal

• The name of the law firm, both addresses, phone number and fax,, The names of the attorneys, the website.
• Fields that get changed such as the date, VIA, Address of who the letter is going to,
• Re, Index,
• should have a clean neat look, sleek
• some color would be nice. A logo of some sort could be nice as well. Maybe a single S or interlocking D's For Dorvik and Dorvik.
• not too modern looking.

```html
<!DOCTYPE html>
<html lang="en">
<head>
<meta charset="utf-8">
<title>Dorvik &amp; Dorvik, llp — Letterhead</title>
<link href="https://fonts.googleapis.com/css2?family=Mulish:wght@400;600;700;800&display=swap" rel="stylesheet">
<style>
  :root {
    --backdrop: #ececec;
    --paper: #ffffff;
    --ink: #2b2e31;
    --ink-soft: #5d6266;
    --brand: #5b7485;
    --brand-light: #8da1ae;
  }
  * { box-sizing: border-box; margin: 0; padding: 0; }
  html, body {
    width: 1200px; height: 1081px; overflow: hidden;
    background: var(--backdrop);
    font-family: "Mulish", "Helvetica Neue", Arial, sans-serif;
    color: var(--ink);
  }
  .letter {
    position: absolute; left: 214px; top: 40px;
    width: 772px; height: 1000px;
    background: var(--paper);
    box-shadow: 0 2px 10px rgba(0,0,0,.08);
    padding: 58px 70px 0 74px;
  }
  .letterhead {
    display: grid;
    grid-template-columns: 190px 200px 1fr;
    column-gap: 26px;
    align-items: start;
  }
  .firm { padding-top: 8px; }
  .firm-mark {
    display: flex; align-items: center; gap: 9px;
  }
  .firm-dot {
    width: 16px; height: 16px; border-radius: 50%;
    background: var(--brand);
  }
  .firm-name {
    font-size: 15px; font-weight: 800; color: var(--brand);
    letter-spacing: .2px;
  }
  .firm-tagline {
    margin: 4px 0 0 25px;
    font-size: 10px; color: var(--brand); letter-spacing: .8px;
  }
  .offices, .attorneys {
    font-size: 9.5px; line-height: 1.45; color: var(--brand);
  }
  .office-label { font-weight: 700; text-transform: uppercase; letter-spacing: .5px; }
  .attorneys li { list-style: none; text-transform: uppercase; letter-spacing: .4px; }
  .attorneys li::before { content: "• "; }
  .attorneys .admission { font-size: 8px; text-transform: none; letter-spacing: 0; padding-left: 10px; }
  .attorneys .admission::before { content: ""; }
  .website { margin-top: 10px; font-size: 9.5px; color: var(--brand); }
  .header-rule {
    margin-top: 22px; height: 0;
    border-top: 2px solid var(--brand);
    border-bottom: 1px solid var(--brand-light);
    padding-top: 2px;
  }
  .reference {
    margin: 34px 0 0 auto; width: 230px;
    font-size: 12px; line-height: 1.4;
    display: grid; grid-template-columns: 46px 1fr;
  }
  .reference dt { font-weight: 800; }
  .letter-body { margin-top: 36px; font-size: 12.5px; line-height: 1.5; }
  .date { text-transform: uppercase; letter-spacing: .6px; }
  .delivery { margin-top: 14px; font-weight: 800; text-transform: uppercase; }
  .recipient { margin-top: 2px; }
  .letter-body p.paragraph { margin-top: 20px; text-align: left; }
  .closing { margin-top: 40px; }
</style>
</head>
<body>
  <main class="letter">
    <header class="letterhead">
      <div class="firm">
        <div class="firm-mark">
          <span class="firm-dot"></span>
          <span class="firm-name">Dorvik &amp; Dorvik, llp</span>
        </div>
        <div class="firm-tagline">Attorneys At Law</div>
      </div>
      <address class="offices">
        48 Halden Street<br>
        New York, New York 10012<br>
        <span class="office-label">Westchester Office</span><br>
        217 Orchard Lane<br>
        Briarwood, New York 10580<br>
        Tel: 555-014-2290<br>
        Fax: 555-014-2291
      </address>
      <div>
        <ul class="attorneys">
          <li>Martin Dorvik, Esq.</li>
          <li>Owen A. Dorvik, Esq.</li>
          <li>Clara Whitfield, Esq.</li>
          <li>Henry T. Marsh, Esq.*</li>
          <li class="admission">* Also admitted in NJ</li>
        </ul>
        <div class="website">www.DorvikLawGroup.com</div>
      </div>
    </header>
    <div class="header-rule"></div>

    <dl class="reference">
      <dt>Re:</dt><dd>XXXXXXXXXXXXXXXXXX</dd>
      <dt>Index:</dt><dd>XXXXXXXX</dd>
    </dl>

    <section class="letter-body">
      <div class="date">Date</div>
      <div class="delivery">Via Lorem Ipsum Dolor Sit Amet</div>
      <div class="recipient">
        XXXXXXXX XXXXXX<br>
        XXXXXXXXXXXXXXXXXX<br>
        XXXXXXXXXX XXXXXXXXX<br>
        XXXXXXXXXX XXXXXXX<br>
        XXXXXXXXXXXXX
      </div>
      <p class="paragraph">Lorem ipsum dolor sit amet, consectetur adipiscing elit. Duis porttitor gravida orci eu varius. In euismod metus vel finibus eleifend. Quisque eu dui, condimentum id cursus eget, ullamcorper nec metus. Vestibulum vitae elementum leo. Suspendisse dictum consequat tempus. Vivamus vel est convallis metus lacinia suscipit sit amet ac tellus. Phasellus quis ligula sit amet libero commodo finibus. Aenean sit condimentum risus. Curabitur egestas nisl vitae hendrerit imperdiet.</p>
      <p class="paragraph">Vestibulum eget congue tortor. Nunc luctus euismod velit, eu aliquet eros. Maecenas suscipit hendrerit orci quis mollis. Aliquam aliquam, urna ac sagittis consequat, ante dolor tempus elit, eu hendrerit velit orci nec tellus. Sed quis placerat massa, a ullamcorper urna. Nullam at ex id mi tincidunt euismod. Mauris sit amet nibh arcu. Vivamus eu fermentum ipsum.</p>
      <p class="paragraph">Maecenas nec mi ipsum. Fusce hendrerit nunc ut felis ultrices, at laoreet est sodales. Aenean convallis mi luctus nunc vulputate, a vulputate dolor eleifend. Cras ornare tellus a convallis dapibus. Mauris et nisl blandit tellus porta dapibus. Cras tempus, libero quis aliquam dignissim, sem diam hendrerit tellus, sit amet finibus tortor arcu id est. Suspendisse porttitor arcu sit amet ante auctor tincidunt. Duis eu porttitor metus.</p>
      <div class="closing">
        Respectfully,<br>
        Owen A. Dorvik
      </div>
    </section>
  </main>
</body>
</html>
```